Basic Letterhead Design

We need a Letterhead design. Our company is in the financial services industry. We are a small bank who lends money. I have uploaded an example our current letterhead design. We would like a new one.

```html
<!DOCTYPE html>
<html lang="en">
<head>
<meta charset="utf-8">
<title>Harlow Lending Letterhead</title>
<link rel="stylesheet" href="https://fonts.googleapis.com/css2?family=Figtree:wght@400;500;600&display=swap">
<style>
  :root {
    --backdrop: #e2e2e2;
    --paper: #ffffff;
    --brand-green: #274b38;
    --ink: #2e2e2e;
    --ink-strong: #151515;
    --signature-tone: #eceeed;
  }
  * { margin: 0; padding: 0; box-sizing: border-box; }
  html, body {
    width: 1200px; height: 1200px; overflow: hidden;
    background: var(--backdrop);
    font-family: "Figtree", sans-serif;
    color: var(--ink);
  }
  .letterhead {
    position: absolute; left: 312px; top: 76px;
    width: 729px; height: 1031px;
    background: var(--paper);
  }
  .brand {
    position: absolute; left: 67px; top: 116px;
    display: flex; align-items: center; gap: 9px;
  }
  .brand-dot { width: 16px; height: 16px; border-radius: 50%; background: var(--brand-green); }
  .brand-name {
    font-size: 22px; font-weight: 600; color: var(--brand-green);
    letter-spacing: 0.02em; line-height: 1;
  }
  .company-registration {
    position: absolute; right: 66px; top: 123px;
    text-align: right; font-size: 9.5px; font-weight: 500;
    line-height: 12px; color: var(--ink-strong);
  }
  .recipient {
    position: absolute; left: 69px; top: 194px;
    font-style: normal;
    font-size: 13px; line-height: 19.6px; color: var(--ink);
  }
  .salutation {
    position: absolute; left: 69px; top: 331px;
    font-size: 13px; line-height: 19.6px; color: var(--ink);
  }
  .letter-body {
    position: absolute; left: 69px; top: 371px; width: 591px;
    font-size: 13px; line-height: 19.6px;
    text-align: justify; color: var(--ink);
  }
  .signature {
    position: absolute; left: 64px; top: 700px;
    width: 275px; height: 69px; border-radius: 6px;
    background: var(--signature-tone);
  }
  .contact {
    position: absolute; left: 70px; top: 933px;
    font-size: 10px; line-height: 14px; color: var(--ink-strong);
  }
  .contact-line { display: flex; align-items: center; gap: 4px; }
  .contact-line svg { width: 7px; height: 7px; fill: var(--brand-green); }
</style>
</head>
<body>
  <main class="letterhead">
    <div class="brand">
      <span class="brand-dot"></span>
      <span class="brand-name">Harlow Lending</span>
    </div>

    <div class="company-registration">
      <p>HARLOW LENDING PTY LTD</p>
      <p>ACN: 512 308 771</p>
    </div>

    <address class="recipient">
      <p>Mr. Alan Reed</p>
      <p>President</p>
      <p>Meridian Accountants</p>
      <p>48 Elm Avenue,</p>
      <p>Fairview State, 54321</p>
    </address>

    <p class="salutation">Dear</p>

    <div class="letter-body">
      <p>Lorem ipsum dolor sit amet, consectetur adipiscing elit. Aenean ut ipsum eget massa hendrerit vestibulum vel in velit. Donec pretium neque velit.</p>
      <p>Aliquam porta lectus nec mauris ornare venenatis. Vivamus non est turpis, et cursus sem. Mauris vehicula erat in diam auctor at bibendum nisl lacinia.</p>
      <p>Morbi imperdiet neque vehicula nunc convallis gravida. Vestibulum iaculis pretium placerat. Integer consequat, est sit amet facilisis eleifend, nibh nibh varius orci, eget dapibus arcu dui non purus. Pellentesque in magna mauris. Duis enim sapien, dictum vitae condimentum a, pulvinar vel lacus. Mauris et molestie nibh. Vestibulum vitae nulla at metus elementum porta sit amet interdum elit. Nulla sollicitudin neque eu nulla volutpat congue.</p>
      <p>Etiam pellentesque, velit id dapibus fermentum, turpis sapien ornare dui, ac tincidunt ligula odio congue purus. Nunc sed ante dui, in porta lectus. Cras nec sem lorem. In hac habitasse platea dictumst. Maecenas id diam quis dui porta tristique. Sed id egestas felis. Donec ullamcorper mattis posuere. Phasellus fermentum eleifend tortor vel dapibus. Vestibulum ante ipsum.</p>
    </div>

    <div class="signature" role="img" aria-label="Handwritten signature of Martin Hale"></div>

    <footer class="contact">
      <p>2200 Harbour Road</p>
      <p>Suite #120 Lakeside, CA, 90210</p>
      <p class="contact-line">
        <svg viewBox="0 0 10 10" aria-hidden="true"><path d="M0 2h10v6H0z M0 2l5 3.5L10 2" fill="var(--brand-green)" stroke="#fff" stroke-width="0.8"/></svg>
        name@harlowlending.com
      </p>
      <p class="contact-line">
        <svg viewBox="0 0 10 10" aria-hidden="true"><path d="M2.2 0.6l1.6 2.2-1 1.1c.6 1.3 1.5 2.2 2.8 2.8l1.1-1 2.2 1.6-.8 1.9C4.7 9.2 0.8 5.3 0.3 1.4z"/></svg>
        300-555-0142
      </p>
    </footer>
  </main>
</body>
</html>
```